New Business Card Design Project VORASTI-Italy

we are VORASTI-Italy
our company in the market for 3 years we are luxury cosmetic company and its about time for a facelift :)
i will like to have elegant luxurious and unique business card
that will give the person that get it a unique, luxurious and elegant impression
I'm VERY OPEN FOR NEW IDEAS , even duo i add a few files of things that i see on line and i like them

i add my logo as well
my website is VORASTI.COM
(if you would like to see the main style that we have)

Target Market(s)

adult that have money :)

Industry/Entity Type

Business

Contact Information for Business Card

Name - Paul Vorasti
Position - CEO and CO Founder
address - 4817 E Larkdale
telephone - 555-384-1962
email - paul@vorasti.com
fax - 555-384-1962
website - VORASTI.COM

Colors
000000
959595
fbee3e
ffffff

Requirements
Must have
• big logo in GOLD color
• elegant look
• impressive
Nice to have
• not must but maybe classy pattern background
• not must but maybe emblem
• maybe clear plastic business card
Should not have
• colors
• images

```html
<!DOCTYPE html>
<html lang="en">
<head>
<meta charset="utf-8">
<title>VORASTI Italy – Business Card</title>
<link rel="stylesheet" href="https://fonts.googleapis.com/css2?family=Tinos:wght@400&family=Roboto:wght@300;400;500&display=swap">
<style>
  :root {
    --stage: #4a3426;
    --card-black: #0d0d0d;
    --card-charcoal: #2a2a2a;
    --gold: #d4ae45;
    --gold-light: #ecd575;
    --gold-deep: #c39d36;
    --ink: #111111;
  }
  html, body {
    margin: 0;
    padding: 0;
    width: 1200px;
    height: 1200px;
    overflow: hidden;
    background: var(--stage);
  }
  .canvas {
    position: relative;
    width: 1200px;
    height: 1200px;
  }
  .card {
    position: absolute;
    left: 225px;
    width: 750px;
    height: 426px;
    display: block;
    box-shadow: 0 18px 30px rgba(0,0,0,0.45);
  }
  .card--front { top: 102px; }
  .card--back { top: 612px; }
  .brand-name { font-family: "Tinos", "Times New Roman", serif; font-weight: 400; fill: var(--gold); }
  .sans { font-family: "Roboto", Arial, sans-serif; fill: var(--gold); }
  .holder-first { font-weight: 300; }
  .holder-last { font-weight: 500; fill: var(--gold-light); }
  .contact-text { font-weight: 400; }
  .hex { fill: var(--gold-light); }
  .icon { fill: var(--ink); }
  .icon-stroke { fill: none; stroke: var(--ink); stroke-width: 2.6; stroke-linecap: round; stroke-linejoin: round; }
</style>
</head>
<body>
<main class="canvas">

  <!-- Front side -->
  <svg class="card card--front" viewBox="0 0 750 426" xmlns="http://www.w3.org/2000/svg">
    <defs>
      <radialGradient id="frontSurface" cx="50%" cy="40%" r="70%">
        <stop offset="0" stop-color="#333333"/>
        <stop offset="1" stop-color="#161616"/>
      </radialGradient>
    </defs>
    <rect class="surface" width="750" height="426" fill="url(#frontSurface)" role="img" aria-label="Dark background with a fine dotted pattern"/>
    <path class="lower-band" d="M0 258 C150 300 300 330 375 330 C450 330 600 300 750 258 L750 426 L0 426 Z" fill="#121212"/>
    <path class="swoosh swoosh--light" d="M0 168 C150 270 300 326 375 326 C450 326 600 270 750 168 L750 210 C600 290 450 328 375 328 C300 328 150 290 0 210 Z" fill="var(--gold-light)"/>
    <path class="swoosh swoosh--deep" d="M0 210 C150 290 300 328 375 328 C450 328 600 290 750 210 L750 258 C600 300 450 330 375 330 C300 330 150 300 0 258 Z" fill="var(--gold-deep)"/>

    <circle class="brand-mark" cx="375" cy="102" r="66" fill="none" stroke="var(--gold)" stroke-width="4"/>
    <text class="brand-name" x="375" y="253" font-size="64" text-anchor="middle" letter-spacing="1">VORASTI</text>
    <rect class="brand-rule" x="220" y="270" width="310" height="3.5" fill="var(--gold)"/>
    <text class="brand-name" x="375" y="305" font-size="24" text-anchor="middle" letter-spacing="1">ITALY</text>

    <text class="sans" x="375" y="389" font-size="19" text-anchor="middle">WWW.VORASTI.COM</text>
  </svg>

  <!-- Back side -->
  <svg class="card card--back" viewBox="0 0 750 426" xmlns="http://www.w3.org/2000/svg">
    <defs>
      <radialGradient id="backSurface" cx="45%" cy="55%" r="70%">
        <stop offset="0" stop-color="#303030"/>
        <stop offset="1" stop-color="#161616"/>
      </radialGradient>
    </defs>
    <rect class="surface" width="750" height="426" fill="url(#backSurface)" role="img" aria-label="Dark background with a fine dotted pattern"/>
    <path class="upper-band" d="M0 0 H750 V70 C600 44 450 36 375 36 C300 36 150 44 0 78 Z" fill="var(--card-black)"/>
    <path class="swoosh swoosh--deep" d="M0 78 C150 44 300 36 375 36 C450 36 600 44 750 70 L750 115 C600 60 450 37 375 37 C300 37 150 70 0 120 Z" fill="var(--gold)"/>
    <path class="swoosh swoosh--light" d="M0 120 C150 70 300 37 375 37 C450 37 600 60 750 115 L750 162 C600 80 450 38 375 38 C300 38 150 90 0 162 Z" fill="var(--gold-light)"/>

    <text class="sans" x="53" y="267" font-size="36">
      <tspan class="holder-first">PAUL </tspan><tspan class="holder-last">VORASTI</tspan>
    </text>
    <text class="sans holder-first" x="73" y="297" font-size="19">CEO AND CO FOUNDER</text>

    <g class="contact" transform="translate(417 156)">
      <polygon class="hex" points="0,-28 24,-14 24,14 0,28 -24,14 -24,-14"/>
      <path class="icon" d="M0 -12 C-6 -12 -9 -7 -9 -3 C-9 3 0 12 0 12 C0 12 9 3 9 -3 C9 -7 6 -12 0 -12 Z M0 -6 A3 3 0 1 0 0.01 -6 Z" fill-rule="evenodd"/>
    </g>
    <text class="sans contact-text" x="455" y="162" font-size="18">4817 E LARKDALE</text>

    <g class="contact" transform="translate(417 226)">
      <polygon class="hex" points="0,-28 24,-14 24,14 0,28 -24,14 -24,-14"/>
      <rect class="icon-stroke" x="-11" y="-2" width="12" height="7" rx="3.5" transform="rotate(-45 -5 1.5)"/>
      <rect class="icon-stroke" x="-1" y="-5" width="12" height="7" rx="3.5" transform="rotate(-45 5 -1.5)"/>
    </g>
    <text class="sans contact-text" x="455" y="232" font-size="18">WWW.VORASTI.COM</text>

    <g class="contact" transform="translate(417 298)">
      <polygon class="hex" points="0,-28 24,-14 24,14 0,28 -24,14 -24,-14"/>
      <rect class="icon-stroke" x="-10" y="-7" width="20" height="14" rx="1"/>
      <path class="icon-stroke" d="M-10 -7 L0 2 L10 -7 M-10 7 L-3 0 M10 7 L3 0"/>
    </g>
    <text class="sans contact-text" x="455" y="304" font-size="18">PAUL@VORASTI.COM</text>

    <g class="contact" transform="translate(417 369)">
      <polygon class="hex" points="0,-28 24,-14 24,14 0,28 -24,14 -24,-14"/>
      <path class="icon" d="M-8 -11 L-3 -11 L-1 -5 L-4 -2 C-2 3 1 6 4 8 L7 5 L12 7 L12 11 C12 12 11 13 9 13 C-2 11 -10 2 -11 -8 C-11 -10 -10 -11 -8 -11 Z"/>
    </g>
    <text class="sans contact-text" x="455" y="375" font-size="18">555-384-1962</text>
  </svg>

</main>
</body>
</html>
```